Stationary for Travel & Tourism Co.
QELVARA Stationary
Stationary for Travel & Tourism Co. - Travel
Creative Brief
Professional
Tariq Hamdoun Salwi
IT Manager
Office No.627, Noor Plaza Al Wardan Dist. - Sahel Tamr Street P.B No.38271 Jeddah 27390 Kingdom of Saudi Arabia
+966 2 6583917 X 482
marwanek@qelvaratrips.com
www.qelvaratrips.com
The horse object in the logo is advised to be nicely embosed as watermark on the stationary particularly on the letter head.

```html
<!DOCTYPE html>
<html lang="en">
<head>
<meta charset="utf-8">
<title>Qelvara Stationary – Business Card</title>
<link rel="stylesheet" href="https://fonts.googleapis.com/css2?family=Montserrat:wght@400;600;800&display=swap">
<style>
  :root{
    --bg:#ffffff;
    --card:#f7f7f7;
    --card-edge:#e2e2e2;
    --brand-red:#b3121c;
    --band-grey:#3a3a3c;
    --ink:#444446;
    --paper-text:#ffffff;
  }
  *{margin:0;padding:0;box-sizing:border-box}
  html,body{width:1200px;height:1009px;overflow:hidden;background:var(--bg)}
  body{position:relative;font-family:"Montserrat",sans-serif}

  .card{
    position:absolute;width:620px;height:354px;border-radius:26px;
    background:var(--card);overflow:hidden;
    box-shadow:0 0 0 1px var(--card-edge);
  }
  .card--back{left:490px;top:110px}
  .card--front{left:90px;top:545px}

  /* back */
  .back-logo{
    position:absolute;left:0;right:0;top:124px;text-align:center;
    color:var(--brand-red);font-weight:800;font-size:54px;letter-spacing:5px;line-height:1;
  }
  .back-web{
    position:absolute;left:0;right:0;top:236px;text-align:center;
    color:var(--ink);font-size:12px;letter-spacing:5px;
  }

  /* front */
  .front-shape{position:absolute;inset:0;width:100%;height:100%}
  .contact{
    position:absolute;left:30px;top:60px;width:250px;
    color:var(--paper-text);font-size:9.5px;line-height:1.65;letter-spacing:.3px;
  }
  .contact .dots{display:flex;gap:6px;margin-bottom:10px}
  .contact .dots span{width:12px;height:12px;border-radius:50%;background:var(--paper-text)}
  .contact p{display:flex;gap:7px;align-items:flex-start}
  .contact svg{flex:none;width:10px;height:10px;margin-top:3px;fill:var(--paper-text)}
  .logo{position:absolute;left:340px;top:148px;width:250px;text-align:center}
  .logo-mark{color:var(--brand-red);font-weight:800;font-size:42px;letter-spacing:3px;line-height:1}
  .logo-sub{color:var(--ink);font-weight:600;font-size:10.5px;letter-spacing:1.2px;margin-top:10px;white-space:nowrap}
  .person{position:absolute;right:34px;bottom:30px;text-align:right}
  .person-name{color:var(--brand-red);font-weight:600;font-size:14px;letter-spacing:2.4px}
  .person-role{color:var(--ink);font-size:9px;letter-spacing:2px;margin-top:5px}
</style>
</head>
<body>

<section class="card card--back">
  <div class="back-logo">QELVARA</div>
  <div class="back-web">www.qelvaratrips.com</div>
</section>

<section class="card card--front">
  <svg class="front-shape" viewBox="0 0 620 354" preserveAspectRatio="none" aria-hidden="true">
    <path d="M0 0 H620 V40 C440 20 340 80 300 190 C270 280 230 330 200 354 H0 Z" fill="var(--brand-red)"/>
    <path d="M620 40 C440 20 340 80 300 190 C270 280 230 330 200 354 H222 C255 330 300 285 332 200 C375 95 460 55 620 66 Z" fill="var(--band-grey)"/>
  </svg>

  <div class="contact">
    <div class="dots"><span></span><span></span><span></span><span></span></div>
    <p><svg viewBox="0 0 10 10"><path d="M5 0a3.5 3.5 0 0 0-3.5 3.5C1.5 6 5 10 5 10s3.5-4 3.5-6.5A3.5 3.5 0 0 0 5 0zm0 5a1.5 1.5 0 1 1 0-3 1.5 1.5 0 0 1 0 3z"/></svg>
      <span>Office No.627, Noor Plaza Al Wardan Dist. - Sahel Tamr Street P.B No.38271 Jeddah 27390<br>Kingdom of Saudi Arabia</span></p>
    <p><svg viewBox="0 0 10 10"><path d="M2 0h2l1 2.5-1.3 1a6 6 0 0 0 2.8 2.8l1-1.3L10 6v2a2 2 0 0 1-2 2A8 8 0 0 1 0 2a2 2 0 0 1 2-2z"/></svg>
      <span>+966 2 6583917 X 482</span></p>
    <p><svg viewBox="0 0 10 10"><path d="M0 2h10v6H0z"/></svg>
      <span>marwanek@qelvaratrips.com</span></p>
    <p><svg viewBox="0 0 10 10"><circle cx="5" cy="5" r="5"/></svg>
      <span>www.qelvaratrips.com</span></p>
  </div>

  <div class="logo">
    <div class="logo-mark">QELVARA</div>
    <div class="logo-sub">QELVARA TRAVEL &amp; TOURISM CO</div>
  </div>

  <div class="person">
    <div class="person-name">Tariq Hamdoun Salwi</div>
    <div class="person-role">IT MANAGER</div>
  </div>
</section>

</body>
</html>
```